Quillstone (real estate analytics tool) - Pavlora and Trembit Cover Page

We are a newly launched SaaS startup which specialises in market analytics for commercial, office and retail property sector: https://quillstone.com.au/
We need two images designed to serve as cover pages for Pavlora and Trembit business pages. The images should be same/similar, however adjusted to fit the cover image specifications of each platform (Pavlora: 1128 (w) x 191 (h) pixels https://www.pavlora.net/help/pavlora/answer/a563309/image-specifications-for-your-pavlora-pages-and-career-pages AND Trembit 1:8 aspect ration https://www.trembit.net/help/125379114252045)
The design should communicate analytics / analysis / people working on computers / perhaps with some playful aspects. The design should utilise our primary green colour (#1c7d39).
The attached screenshot shows the first attempt which we DO NOT like. It has no flow, it feels broken, the way the profile picture overlays the cover image is not great and feels broken.
Real Estate
- Caviar Dreams, Comfortaa

```html
<!DOCTYPE html>
<html lang="en">
<head>
<meta charset="utf-8">
<title>Quillstone Cover</title>
<link rel="stylesheet" href="https://fonts.googleapis.com/css2?family=Comfortaa:wght@400;500;700&display=swap">
<style>
  :root {
    --bg: #ffffff;
    --ink: #3a3a3a;
    --ink-soft: #444444;
    --lime: #5ce51c;
    --lime-light: #b4f58c;
    --brand-green: #1c7d39;
    --chart-grey: #f1f1f1;
    --chart-line: #ececec;
    --shadow-black: #0d0d0d;
    --photo-a: #d9dde0;
    --photo-b: #8f8a86;
  }
  html, body {
    margin: 0;
    padding: 0;
    overflow: hidden;
    background: var(--bg);
  }
  .cover {
    position: relative;
    width: 1200px;
    height: 203px;
    overflow: hidden;
    background: var(--bg);
    font-family: "Comfortaa", sans-serif;
  }
  .cover-art {
    position: absolute;
    inset: 0;
    width: 1200px;
    height: 203px;
  }
  .brand {
    position: absolute;
    left: 128px;
    top: 49px;
    display: flex;
    align-items: center;
    gap: 10px;
  }
  .brand-dot {
    width: 28px;
    height: 28px;
    border-radius: 50%;
    background: var(--lime);
  }
  .brand-name {
    font-family: "Comfortaa", sans-serif;
    font-weight: 500;
    font-size: 27px;
    color: var(--ink);
    letter-spacing: 0.2px;
  }
  .headline {
    position: absolute;
    left: 125px;
    top: 100px;
    margin: 0;
    font-family: "Comfortaa", sans-serif;
    font-weight: 500;
    font-size: 23px;
    color: var(--ink);
    letter-spacing: 0.1px;
  }
  .tagline {
    position: absolute;
    left: 125px;
    top: 134px;
    margin: 0;
    font-family: "Comfortaa", sans-serif;
    font-weight: 400;
    font-size: 16.5px;
    color: var(--ink-soft);
  }
</style>
</head>
<body>
  <div class="cover">
    <svg class="cover-art" viewBox="0 0 1128 191" preserveAspectRatio="none" xmlns="http://www.w3.org/2000/svg">
      <defs>
        <linearGradient id="team-photo-tone" x1="0" y1="0" x2="1" y2="1">
          <stop offset="0" stop-color="var(--photo-a)"/>
          <stop offset="1" stop-color="var(--photo-b)"/>
        </linearGradient>
      </defs>

      <!-- faint background chart -->
      <g class="bg-chart">
        <rect x="240" y="165" width="38" height="26" fill="var(--chart-grey)"/>
        <rect x="292" y="122" width="38" height="69" fill="var(--chart-grey)"/>
        <rect x="344" y="92" width="38" height="99" fill="var(--chart-grey)"/>
        <rect x="396" y="55" width="38" height="136" fill="var(--chart-grey)"/>
        <polyline points="140,190 200,120 250,98 300,62 380,14 440,4"
                  fill="none" stroke="var(--chart-line)" stroke-width="3"/>
        <circle cx="200" cy="120" r="5" fill="var(--chart-line)"/>
        <circle cx="300" cy="62" r="5" fill="var(--chart-line)"/>
        <circle cx="380" cy="14" r="5" fill="var(--chart-line)"/>
      </g>

      <!-- left edge accents -->
      <polygon class="accent-left" points="0,33 68,33 0,118" fill="var(--lime)"/>
      <polygon class="accent-left-soft" points="0,64 58,64 0,140" fill="var(--lime-light)"/>

      <!-- team photo area -->
      <polygon points="700,0 1128,0 1128,191 622,191" fill="url(#team-photo-tone)"
               role="img" aria-label="Photo of a team of colleagues meeting around a table with a laptop in a bright office"/>

      <!-- divider accents -->
      <polygon class="accent-divider" points="688,0 724,0 640,112 604,112" fill="var(--lime)"/>
      <polygon class="accent-divider-soft" points="650,60 676,60 612,150 586,150" fill="var(--lime-light)"/>
      <polygon class="accent-shadow" points="608,191 690,191 690,96" fill="var(--shadow-black)"/>
    </svg>

    <div class="brand">
      <span class="brand-dot"></span>
      <span class="brand-name">quillstone</span>
    </div>
    <h1 class="headline">Are you ready to save time and energy?</h1>
    <p class="tagline">Just imagine your productivity boost with this one tool!</p>
  </div>
</body>
</html>
```